Banner Ad Design Project

We need a Banner to hang outside our Health Food Store to advertise to the public that we will be holding an Organic Market Day every Saturday.
We have our Business name and logo that will need to be incorporated into the design.
We want the design to convey freshness and have an earthy / farm feel, but also want the design to be crisp and not "Hippie"
we also need the banner to say "Fresh Organic Market every Saturday"
we will be selling fresh organic fruit and vegetables.
Target Market(s)
existing customers and general public walking past the shop
Industry/Entity Type
Farm
Look and feel
Each slider illustrates characteristics of the customer's brand and the style your logo design should communicate.

```html
<!DOCTYPE html>
<html lang="en">
<head>
<meta charset="utf-8">
<title>Harrowgate Wholefoods Store – Organic Market Every Saturday</title>
<link rel="stylesheet" href="https://fonts.googleapis.com/css2?family=Marcellus&family=Yellowtail&family=Courgette&display=swap">
<style>
  :root {
    --wood-light: #dcb98a;
    --wood-mid: #c79a63;
    --wood-dark: #a97944;
    --night: #050505;
    --brand-brown: #a3421f;
    --organic-green: #2f9a3a;
    --organic-edge: #ffffff;
    --fresh-blue: #1fa3e8;
    --headline-white: #ffffff;
    --headline-red: #c8161d;
    --basket-warm: #b7783a;
    --basket-veg: #e0813a;
  }
  html, body {
    margin: 0;
    padding: 0;
    overflow: hidden;
    background: #ffffff;
  }
  .banner {
    position: relative;
    width: 1200px;
    height: 720px;
    overflow: hidden;
    font-family: "Marcellus", serif;
  }
  .wood-backdrop {
    position: absolute;
    inset: 0;
    background: linear-gradient(100deg, var(--wood-dark) 0%, var(--wood-light) 40%, var(--wood-mid) 75%, var(--wood-dark) 100%);
  }
  .night-field {
    position: absolute;
    inset: 0;
  }
  .produce-basket {
    position: absolute;
    left: 0;
    top: 0;
    width: 460px;
    height: 335px;
    border-radius: 0 0 48% 42% / 0 0 30% 30%;
    background: radial-gradient(ellipse at 45% 30%, var(--basket-veg) 0%, #e9d7b4 35%, var(--basket-warm) 70%, #8a5424 100%);
  }
  .store-name {
    position: absolute;
    left: 500px;
    top: 28px;
    width: 620px;
    margin: 0;
    text-align: center;
    color: var(--brand-brown);
    font-family: "Marcellus", serif;
    font-weight: 400;
    font-size: 72px;
    line-height: 1;
    letter-spacing: 1px;
  }
  .store-name span { display: block; }
  .organic-word {
    position: absolute;
    left: 55px;
    top: 280px;
    margin: 0;
    font-family: "Yellowtail", cursive;
    font-weight: 400;
    font-size: 150px;
    line-height: 1;
    color: var(--organic-green);
    -webkit-text-stroke: 3px var(--organic-edge);
    paint-order: stroke fill;
    text-shadow: 4px 5px 0 rgba(0,0,0,0.35);
    transform: rotate(-9deg);
    transform-origin: left center;
  }
  .fresh-word {
    position: absolute;
    left: 610px;
    top: 305px;
    margin: 0;
    font-family: "Courgette", cursive;
    font-size: 64px;
    line-height: 1;
    color: var(--fresh-blue);
  }
  .headline {
    position: absolute;
    margin: 0;
    font-family: "Marcellus", serif;
    font-weight: 400;
    color: var(--headline-white);
    text-shadow: 5px 5px 0 var(--headline-red);
    line-height: 1;
    white-space: nowrap;
  }
  .headline-market {
    left: 485px;
    top: 388px;
    font-size: 150px;
  }
  .headline-day {
    left: 48px;
    top: 556px;
    font-size: 138px;
  }
</style>
</head>
<body>
  <main class="banner">
    <div class="wood-backdrop" role="img" aria-label="Warm light wooden plank background"></div>

    <svg class="night-field" width="1200" height="720" viewBox="0 0 1200 720" aria-hidden="true">
      <path d="M0 400 Q 380 250 760 292 Q 1000 300 1200 318 L1200 720 L0 720 Z" fill="var(--night)"/>
    </svg>

    <div class="produce-basket" role="img" aria-label="Wicker basket filled with carrots, parsnips, potatoes and green beans"></div>

    <h1 class="store-name"><span>harrowgate</span><span>wholefoods store</span></h1>

    <p class="organic-word">Organic</p>
    <p class="fresh-word">Fresh</p>
    <p class="headline headline-market">MARKET</p>
    <p class="headline headline-day">EVERY SATURDAY</p>
  </main>
</body>
</html>
```